Norvel Construction Co
Stationary & Bus Card for Building Company - Construction
Stationary & Bus Card for Building Company
Use standard fonts
Flexible regarding fonts. Need to be professional
Professional
Dean M. Kowalczykson
Executive Director
Suite 4, 718 Pinecrest Avenue Lindale, Australia 3217
Mobile: 0427 519 284
dean@norvelco.com.au
norvelco.com.au
The business card must be 55mm (high) x 90mm (wide). Letter Head - paper A4 size Please include the following items: (a) "With Compliments" slip. (b) Document Folder or Wallet - A4 size
Icon and logo only
QuietHarbour QuietHarbour
We have received a few good options so far. We would also like to see more options using different colours. We are looking for something that is cutting edge and has a Wow factor. For example the document folder does not need to have the same colour or format as the business card. We are looking for something more impressive here, because we want our clients to be impressed. For example, using embossed icon or logo, and textured background. We want to portray an image that is Creative and prestigious. Surprise me!
We have received a few good options so far. We would like to see more options using different colours. We looking for something that is cutting edge and has a Wow
Update: please add space on the card for credentials/qualifications as follows: Dean M. Kowalczyksonn, PhD "PhD" should be in a smaller font and not in bold (same font as title)

```html
<!DOCTYPE html>
<html lang="en">
<head>
<meta charset="utf-8">
<title>Norvel Construction Co – Stationery Set</title>
<link href="https://fonts.googleapis.com/css2?family=Montserrat:wght@400;600&display=swap" rel="stylesheet">
<style>
:root{
  --backdrop:#3a302a;
  --paper:#ffffff;
  --red:#c4161c;
  --red-deep:#6e0a0d;
  --charcoal:#1f1f21;
  --charcoal-2:#343437;
  --ink:#2b2b2b;
  --faint-red:rgba(196,22,28,.13);
  --faint-grey:rgba(60,60,60,.13);
}
*{box-sizing:border-box;margin:0;padding:0}
html,body{width:1200px;height:310px;overflow:hidden}
body{background:var(--backdrop);position:relative;font-family:"Montserrat",Arial,sans-serif;color:var(--ink)}
.piece{position:absolute;overflow:hidden;box-shadow:0 3px 8px rgba(0,0,0,.45)}

/* business cards */
.card{width:96px;height:58px;border-radius:1px}
.card--front{left:12px;top:162px;background:var(--paper);display:flex;flex-direction:column;justify-content:center;align-items:center;gap:3px}
.card--back{left:12px;top:226px;background:var(--paper);padding:7px 6px}
.brand{font-weight:600;color:var(--red);letter-spacing:.04em;text-transform:uppercase;white-space:nowrap}
.brand-mark{display:flex;align-items:center;gap:3px}
.brand-mark i{display:block;background:var(--red);flex:none}
.card .brand{font-size:5px}
.card .brand-mark i{width:6px;height:6px}
.card-name{font-size:4.6px;font-weight:600;line-height:1.3}
.card-name small{font-weight:400;font-size:3.4px}
.card-role,.card-line{font-size:3.4px;line-height:1.35}
.red-band{position:absolute;left:0;right:0;bottom:0;background:linear-gradient(90deg,var(--red-deep),var(--red) 55%,var(--red-deep))}
.card .red-band{height:9px}

/* letterheads */
.letterhead{top:19px;width:198px;height:264px;background:var(--paper)}
.letterhead--one{left:132px}
.letterhead--two{left:346px}
.letterhead .brand-mark{position:absolute;top:14px;left:50%;transform:translateX(-50%)}
.letterhead .brand{font-size:5.5px}
.letterhead .brand-mark i{width:6px;height:6px}
.watermark{position:absolute;left:8px;right:8px;top:92px;text-align:center;font-weight:600;font-size:17px;line-height:1.2;text-transform:uppercase;letter-spacing:.02em}
.letterhead--one .watermark{color:var(--faint-red)}
.letterhead--two .watermark{color:var(--faint-grey)}
.band-curve{position:absolute;left:0;bottom:0;width:100%;height:34px}

/* envelopes */
.envelope{left:553px;width:196px}
.envelope--flap-a{top:108px;height:54px;background:var(--paper)}
.envelope--flap-b{top:170px;height:52px;background:var(--paper)}
.envelope--plain{top:228px;height:48px;background:var(--paper)}
.envelope svg{position:absolute;inset:0;width:100%;height:100%}
.envelope .brand-mark{position:absolute;left:50%;transform:translateX(-50%);top:12px}
.envelope .brand{font-size:5px;color:#fff}
.envelope .brand-mark i{width:6px;height:6px;background:#fff}
.envelope--plain .brand-mark{top:6px;left:8px;transform:none}
.envelope--plain .brand{color:var(--red)}
.envelope--plain .brand-mark i{background:var(--red)}

/* folders */
.folder{top:24px;width:208px;height:259px;display:flex;align-items:center;justify-content:center}
.folder--dark{left:763px;background:radial-gradient(ellipse at 50% 40%,var(--charcoal-2),var(--charcoal) 75%)}
.folder--red{left:980px;background:radial-gradient(ellipse at 50% 40%,var(--red),var(--red-deep) 90%)}
.folder .brand{font-size:16px;text-align:center;line-height:1.2;white-space:normal}
.folder--dark .brand{color:var(--red)}
.folder--red .brand{color:var(--charcoal)}
</style>
</head>
<body>

<div class="piece card card--front">
  <div class="brand-mark"><i></i><span class="brand">Norvel Construction Co</span></div>
  <div class="red-band"></div>
</div>

<div class="piece card card--back">
  <p class="card-name">Dean M. Kowalczyksonn <small>PhD</small></p>
  <p class="card-role">Executive Director</p>
  <p class="card-line">Suite 4, 718 Pinecrest Avenue Lindale, Australia 3217</p>
  <p class="card-line">Mobile: 0427 519 284 · dean@norvelco.com.au</p>
  <div class="red-band"></div>
</div>

<div class="piece letterhead letterhead--one">
  <div class="brand-mark"><i></i><span class="brand">Norvel Construction Co</span></div>
  <p class="watermark">Norvel<br>Construction<br>Co</p>
  <svg class="band-curve" viewBox="0 0 198 34" preserveAspectRatio="none" aria-hidden="true">
    <path d="M0 12 Q100 4 198 18 L198 34 L0 34 Z" fill="#c4161c"/>
    <path d="M0 20 Q90 10 198 26 L198 34 L0 34 Z" fill="#6e0a0d"/>
  </svg>
</div>

<div class="piece letterhead letterhead--two">
  <div class="brand-mark"><i></i><span class="brand">Norvel Construction Co</span></div>
  <p class="watermark">Norvel<br>Construction<br>Co</p>
  <svg class="band-curve" viewBox="0 0 198 34" preserveAspectRatio="none" aria-hidden="true">
    <path d="M0 18 Q110 8 198 12 L198 34 L0 34 Z" fill="#c4161c"/>
    <path d="M0 26 Q100 16 198 22 L198 34 L0 34 Z" fill="#6e0a0d"/>
  </svg>
</div>

<div class="piece envelope envelope--flap-a">
  <svg viewBox="0 0 196 54" preserveAspectRatio="none" aria-hidden="true">
    <path d="M0 0 H196 V8 L98 48 L0 8 Z" fill="#c4161c"/>
  </svg>
  <div class="brand-mark"><i></i><span class="brand">Norvel Construction Co</span></div>
</div>

<div class="piece envelope envelope--flap-b">
  <svg viewBox="0 0 196 52" preserveAspectRatio="none" aria-hidden="true">
    <path d="M0 0 H196 V6 L98 44 L0 6 Z" fill="#6e0a0d"/>
  </svg>
  <div class="brand-mark"><i></i><span class="brand">Norvel Construction Co</span></div>
</div>

<div class="piece envelope envelope--plain">
  <div class="brand-mark"><i></i><span class="brand">Norvel Construction Co</span></div>
</div>

<div class="piece folder folder--dark">
  <span class="brand">Norvel<br>Construction Co</span>
</div>

<div class="piece folder folder--red">
  <span class="brand">Norvel<br>Construction Co</span>
</div>

</body>
</html>
```